Coffeeshop menu for filter tip

We want to have a cannabis (coffeeshop) menu in the size 25mm wide x 60mm wide. Some examples attached.

it must have the following text:
Menu

WEED p/g
Velotrine €16
Cinderfox €14
Tide Rambler €14
Marigolden €16
Grand Pelican €14
Copper Comet €14

HASH p/g
Baltic Ember €12
Harbor Velvet€11
Plum Rova €14
Dusk Maple €10

Target Market(s)

tourist in Amsterdam

Requirements
Nice to have
• cannabis sign leaf
• No Cigarettes allowed symbol

```html
<!DOCTYPE html>
<html lang="en">
<head>
<meta charset="utf-8">
<title>Amsterdam Menu</title>
<link rel="stylesheet" href="https://fonts.googleapis.com/css2?family=Lobster&family=Open+Sans:wght@400&display=swap">
<style>
  :root {
    --wood-light: #9a9d9b;
    --wood-mid: #7f8382;
    --wood-dark: #5d6261;
    --leaf-light: #8fd35a;
    --leaf-dark: #2f8a2a;
    --title-dark: #2a1a16;
    --title-red: #8e1c12;
    --outline-green: #3fa236;
    --item-white: #fbfaf5;
    --item-shadow: rgba(30, 20, 15, 0.85);
    --note-grey: #c9cbca;
    --sign-red: #d42a1f;
  }
  html, body {
    margin: 0;
    padding: 0;
    width: 1200px;
    height: 2884px;
    overflow: hidden;
  }
  .menu-card {
    position: relative;
    width: 1200px;
    height: 2884px;
    overflow: hidden;
    font-family: "Lobster", cursive;
  }
  .wood-background {
    position: absolute;
    inset: 0;
    background:
      repeating-linear-gradient(90deg, rgba(255,255,255,0.05) 0 14px, rgba(0,0,0,0.05) 14px 30px),
      linear-gradient(90deg, var(--wood-mid), var(--wood-light) 35%, var(--wood-mid) 55%, var(--wood-light) 80%, var(--wood-dark));
  }
  .leaf {
    position: absolute;
    border-radius: 50%;
    background: radial-gradient(ellipse at 40% 40%, var(--leaf-light), var(--leaf-dark));
    opacity: 0.9;
  }
  .leaf-top { left: -40px; top: -60px; width: 900px; height: 760px; transform: rotate(20deg); border-radius: 45% 55% 60% 40%; }
  .leaf-bottom { left: 250px; top: 1780px; width: 1050px; height: 1150px; transform: rotate(-15deg); border-radius: 55% 45% 40% 60%; }
  .leaf-small { width: 180px; height: 170px; opacity: 0.55; background: radial-gradient(ellipse, #6b8a3a, #8a3a2a); }
  .leaf-small.one { left: 930px; top: 90px; }
  .leaf-small.two { left: 860px; top: 540px; }
  .leaf-small.three { left: 890px; top: 1700px; }

  .title {
    position: absolute;
    left: 0; width: 1200px;
    top: 40px;
    margin: 0;
    text-align: center;
    font-size: 172px;
    font-weight: 400;
    line-height: 1;
    color: var(--title-dark);
    -webkit-text-stroke: 5px var(--item-white);
    paint-order: stroke fill;
    text-shadow: 6px 6px 0 var(--outline-green);
  }
  .subtitle {
    position: absolute;
    left: 640px;
    top: 215px;
    margin: 0;
    font-size: 104px;
    line-height: 1;
    color: var(--title-red);
    text-shadow: 5px 5px 0 var(--outline-green);
  }
  .section-title {
    position: absolute;
    left: 150px;
    margin: 0;
    font-size: 150px;
    font-weight: 400;
    line-height: 1;
    color: var(--title-dark);
    -webkit-text-stroke: 4px var(--item-white);
    paint-order: stroke fill;
    text-shadow: 6px 6px 0 var(--outline-green);
  }
  .section-weed { top: 655px; }
  .section-hash { top: 1745px; }

  .price-list {
    position: absolute;
    left: 160px;
    width: 900px;
    margin: 0;
    padding: 0;
    list-style: none;
  }
  .price-list.weed { top: 870px; }
  .price-list.hash { top: 1995px; }
  .price-item {
    display: flex;
    justify-content: space-between;
    height: 134px;
    align-items: center;
    font-size: 86px;
    color: var(--item-white);
    text-shadow: 4px 4px 4px var(--item-shadow);
  }
  .price-list.hash .price-item { height: 137px; }
  .price-item .price { width: 170px; text-align: left; }

  .no-smoking {
    position: absolute;
    left: 70px;
    top: 2675px;
    display: flex;
    align-items: center;
    gap: 22px;
  }
  .no-smoking-note {
    font-family: "Open Sans", sans-serif;
    font-size: 44px;
    line-height: 1.2;
    color: var(--note-grey);
    margin: 0;
  }
</style>
</head>
<body>
  <main class="menu-card">
    <div class="wood-background" role="img" aria-label="Weathered grey wooden planks background"></div>
    <div class="leaf leaf-top" role="img" aria-label="Large green cannabis leaf"></div>
    <div class="leaf leaf-bottom" role="img" aria-label="Large green cannabis leaf"></div>
    <div class="leaf leaf-small one" role="img" aria-label="Small faded cannabis leaf"></div>
    <div class="leaf leaf-small two" role="img" aria-label="Small faded cannabis leaf"></div>
    <div class="leaf leaf-small three" role="img" aria-label="Small faded cannabis leaf"></div>

    <h1 class="title">Amsterdam</h1>
    <p class="subtitle">menu</p>

    <h2 class="section-title section-weed">Weed</h2>
    <ul class="price-list weed">
      <li class="price-item"><span class="name">Velotrine</span><span class="price">€16</span></li>
      <li class="price-item"><span class="name">Cinderfox</span><span class="price">€14</span></li>
      <li class="price-item"><span class="name">Tide Rambler</span><span class="price">€14</span></li>
      <li class="price-item"><span class="name">Marigolden</span><span class="price">€16</span></li>
      <li class="price-item"><span class="name">Grand Pelican</span><span class="price">€14</span></li>
      <li class="price-item"><span class="name">Copper Comet</span><span class="price">€14</span></li>
    </ul>

    <h2 class="section-title section-hash">Hash</h2>
    <ul class="price-list hash">
      <li class="price-item"><span class="name">Baltic Ember</span><span class="price">€12</span></li>
      <li class="price-item"><span class="name">Harbor Velvet</span><span class="price">€11</span></li>
      <li class="price-item"><span class="name">Plum Rova</span><span class="price">€14</span></li>
      <li class="price-item"><span class="name">Dusk Maple</span><span class="price">€10</span></li>
    </ul>

    <div class="no-smoking">
      <svg width="140" height="140" viewBox="0 0 140 140" aria-hidden="true">
        <circle cx="70" cy="70" r="64" fill="#ffffff"/>
        <rect x="28" y="64" width="74" height="14" fill="#333"/>
        <rect x="102" y="64" width="12" height="14" fill="#333"/>
        <path d="M104 58 q6 -10 0 -20" stroke="#333" stroke-width="4" fill="none"/>
        <circle cx="70" cy="70" r="58" fill="none" stroke="var(--sign-red)" stroke-width="12"/>
        <line x1="29" y1="29" x2="111" y2="111" stroke="var(--sign-red)" stroke-width="12"/>
      </svg>
      <p class="no-smoking-note">No Cigarettes<br>allowed</p>
    </div>
  </main>
</body>
</html>
```